Stationary Package for Construction Company
Modern and Professional
Stationary Package for Construction Company - Construction
Creative Brief
Professional
Karl T. Wentworth
V.P., Operations & Sr. Project Manager
7148 Orchard Lane, Unit 512 Myrtle Beach, SC 29614
843.555.0178 ext. 214
Karl@BrimstackLLC.example
www.BrimstackLLC.example
Current logo is uploaded in .ai format. If color needs to be altered, that is ok. We may also need an alternate color for back of business card. I have also uploaded a few card samples that we already like.
Back of card should be alternate color, either red or black. Two options: One card back with logo only, and one version with logo, web address and services rendered, which I'll specify in greater detail as we narrow down specific designs that we like.

```html
<!DOCTYPE html>
<html lang="en">
<head>
<meta charset="utf-8">
<title>Brimstack Construction – Business Card</title>
<link href="https://fonts.googleapis.com/css2?family=Roboto+Condensed:wght@400;700;900&display=swap" rel="stylesheet">
<style>
  :root {
    --bg: #5b5b5b;
    --brick-light: #b23a24;
    --brick-dark: #7c2114;
    --red: #e0241f;
    --black: #141414;
    --white: #ffffff;
    --paper: #f7f7f7;
    --muted: #d9d9d9;
  }
  * { margin: 0; padding: 0; box-sizing: border-box; }
  html, body { width: 1200px; height: 908px; overflow: hidden; }
  body {
    background: var(--bg);
    font-family: "Roboto Condensed", Arial, sans-serif;
    position: relative;
  }
  .card {
    position: absolute;
    width: 520px;
    height: 300px;
    border-radius: 18px;
    overflow: hidden;
    box-shadow: 0 10px 26px rgba(0,0,0,.35);
  }
  /* front */
  .card-front { left: 60px; top: 170px; }
  .brick-fill {
    position: absolute; inset: 0;
    background: linear-gradient(135deg, var(--brick-light), var(--brick-dark));
  }
  .front-brand {
    position: absolute; left: 0; right: 0; top: 104px;
    text-align: center; color: var(--white);
  }
  .brand-name {
    font-weight: 900; font-size: 36px; line-height: 1; letter-spacing: 1px;
    text-transform: uppercase;
  }
  .brand-values {
    margin-top: 14px; font-weight: 700; font-size: 19px; letter-spacing: 1.5px;
  }
  /* back */
  .card-back { left: 620px; top: 430px; background: var(--paper); }
  .wave { position: absolute; inset: 0; }
  .contact {
    position: absolute; left: 262px; top: 18px; width: 236px;
    color: var(--white); font-size: 12px; line-height: 1.4;
  }
  .contact-name { font-weight: 700; font-size: 18px; line-height: 1.2; margin-bottom: 2px; }
  .contact-title { color: var(--muted); margin-bottom: 8px; }
  .contact-line { display: flex; align-items: flex-start; gap: 7px; }
  .contact-line svg { width: 11px; height: 11px; flex: none; margin-top: 3px; }
  .back-brand {
    position: absolute; left: 28px; bottom: 30px; color: var(--red);
  }
  .back-brand .brand-name { font-size: 28px; }
  .back-brand .brand-values { font-size: 15px; margin-top: 9px; }
</style>
</head>
<body>

<section class="card card-front">
  <div class="brick-fill" role="img" aria-label="Red brick wall texture"></div>
  <div class="front-brand">
    <div class="brand-name">Brimstack<br>Construction</div>
    <div class="brand-values">QUALITY · SERVICE · PRICE</div>
  </div>
</section>

<section class="card card-back">
  <svg class="wave" width="520" height="300" viewBox="0 0 520 300" aria-hidden="true">
    <path d="M0,0 H520 V270 C470,267 430,240 390,225 C320,205 250,215 210,185 C170,145 90,120 0,120 Z" fill="var(--red)"/>
    <path d="M0,0 H520 V256 C470,253 430,226 390,211 C320,191 250,201 210,171 C170,131 90,106 0,106 Z" fill="var(--black)"/>
  </svg>
  <div class="contact">
    <div class="contact-name">Karl T. Wentworth</div>
    <div class="contact-title">V.P., Operations &amp;<br>Sr. Project Manager</div>
    <div class="contact-line">
      <svg viewBox="0 0 12 12"><path d="M6 0a4 4 0 0 0-4 4c0 3 4 8 4 8s4-5 4-8a4 4 0 0 0-4-4zm0 5.5A1.5 1.5 0 1 1 6 2.5a1.5 1.5 0 0 1 0 3z" fill="var(--red)"/></svg>
      <span>7148 Orchard Lane, Unit 512<br>Myrtle Beach, SC 29614</span>
    </div>
    <div class="contact-line">
      <svg viewBox="0 0 12 12"><path d="M2.5 0.5l2 2-1 1.5a7 7 0 0 0 4.5 4.5l1.5-1 2 2-1.5 2C5 11 1 7 .5 2z" fill="var(--red)"/></svg>
      <span>843.555.0178 ext. 214</span>
    </div>
    <div class="contact-line">
      <svg viewBox="0 0 12 12"><rect x="0.5" y="2" width="11" height="8" fill="none" stroke="var(--red)"/><path d="M.5 2.5L6 7l5.5-4.5" fill="none" stroke="var(--red)"/></svg>
      <span>Karl@BrimstackLLC.example</span>
    </div>
    <div class="contact-line">
      <svg viewBox="0 0 12 12"><circle cx="6" cy="6" r="5.3" fill="none" stroke="var(--red)"/><path d="M.7 6h10.6M6 .7c-3 3-3 7.6 0 10.6M6 .7c3 3 3 7.6 0 10.6" fill="none" stroke="var(--red)"/></svg>
      <span>www.BrimstackLLC.example</span>
    </div>
  </div>
  <div class="back-brand">
    <div class="brand-name">Brimstack<br>Construction</div>
    <div class="brand-values">QUALITY · SERVICE · PRICE</div>
  </div>
</section>

</body>
</html>
```